Business Cards Design for the electrical wholesaler: clean bold dynamic :)

We need a business card design that would follow our latest brand guidelines. As an electrical wholesaler we want to bring a fresh look and feel into the industry. The design should be clean bold and dynamic. It should come alive with the renewed energy of our green colour. Our grey colour should keep things balanced and complement the notion of maturity and responsibility. We employ Lato as a corporate font however are not bound by this font and we’re open to interpretation here.

Target Market(s)

Electrical contractors

Industry/Entity Type

Business

Contact Information for Business Card

Logo
Name & Surname: Olena Dovbush
Job Title: Director of Marketing
Email: helen.dovbush@mailvane.example
Cell phone: XXX.XXX.XXXX
Address: 20917 - 87 Ave. Edmonton, AB, Canada. T6K 2R8
Business Phone: 780.555.0187
Website: www.qorvil.example

Font styles to use
Other font styles liked:
• Lato

Requirements
Must have
• Logo & website
Nice to have
• Brand elements - some of them you may find in the attached Brand Guidelines (e.g. three lines on the background signifying "W")

```html
<!DOCTYPE html>
<html lang="en">
<head>
<meta charset="utf-8">
<title>Qorvil Electrical Wholesalers – Business Card</title>
<link rel="stylesheet" href="https://fonts.googleapis.com/css2?family=Lato:wght@400;700;900&display=swap">
<style>
  :root {
    --green: #7dc242;
    --green-dark: #6aae33;
    --charcoal: #3d3e40;
    --ink: #3a3b3d;
    --white: #ffffff;
    --stage: #c8c8c8;
  }
  * { box-sizing: border-box; margin: 0; padding: 0; }
  html, body {
    width: 1200px; height: 1200px; overflow: hidden;
    background: var(--stage);
    font-family: "Lato", Arial, sans-serif;
  }
  .canvas {
    position: relative; width: 1200px; height: 1200px;
  }
  .card {
    position: absolute; top: 436px;
    width: 540px; height: 327px;
    overflow: hidden;
    box-shadow: 0 2px 6px rgba(0,0,0,.18);
  }
  /* ---------- front ---------- */
  .card--front { left: 40px; background: var(--white); }
  .brand {
    position: absolute; display: flex; flex-direction: column; align-items: flex-end;
  }
  .card--front .brand { right: 26px; top: 22px; }
  .brand__row { display: flex; align-items: center; gap: 10px; }
  .brand__dot {
    width: 34px; height: 34px; border-radius: 50%; background: var(--green);
  }
  .brand__name {
    font-weight: 700; font-size: 50px; line-height: 1; letter-spacing: -1px;
    color: var(--ink);
  }
  .brand__tagline {
    margin-top: 3px;
    font-size: 9.5px; font-weight: 700; letter-spacing: 1.2px;
    color: var(--green-dark); text-transform: uppercase;
  }
  .person { position: absolute; left: 24px; top: 128px; }
  .person__name { font-size: 27px; color: var(--ink); line-height: 1.1; }
  .person__name b { font-weight: 700; }
  .person__name span { font-weight: 400; }
  .person__title { margin-top: 4px; font-size: 15px; color: var(--green-dark); font-weight: 400; }
  .divider {
    position: absolute; left: 0; right: 0; top: 196px; height: 4px; background: var(--charcoal);
  }
  .contact-band {
    position: absolute; left: 0; right: 0; top: 204px; bottom: 0; background: var(--green);
  }
  .contact {
    position: absolute; display: flex; align-items: flex-start; gap: 9px;
    font-size: 15.5px; color: var(--ink); line-height: 1.25;
  }
  .contact svg { flex: none; width: 17px; height: 17px; margin-top: 1px; }
  .contact--address { left: 22px; top: 20px; width: 320px; }
  .contact--email { left: 22px; top: 84px; }
  .contact--web { left: 370px; top: 18px; font-weight: 700; }
  .contact--phone { left: 370px; top: 50px; font-weight: 700; }
  .contact--mobile { left: 370px; top: 84px; font-weight: 700; }
  /* ---------- back ---------- */
  .card--back { left: 620px; background: var(--charcoal); }
  .card--back .brand { left: 50%; top: 50%; transform: translate(-50%, -50%); }
  .card--back .brand__name { color: var(--white); }
  .card--back .brand__tagline { color: var(--green); }
  .back__web {
    position: absolute; left: 22px; bottom: 18px;
    font-size: 13px; font-weight: 700; letter-spacing: .6px; color: var(--green);
  }
</style>
</head>
<body>
<main class="canvas">

  <section class="card card--front" aria-label="Business card front">
    <div class="brand">
      <div class="brand__row">
        <div class="brand__dot"></div>
        <div class="brand__name">qorvil</div>
      </div>
      <div class="brand__tagline">Electrical Wholesalers</div>
    </div>

    <div class="person">
      <p class="person__name"><b>Olena</b> <span>Dovbush</span></p>
      <p class="person__title">Director of Marketing</p>
    </div>

    <div class="divider"></div>

    <div class="contact-band">
      <p class="contact contact--address">
        <svg viewBox="0 0 20 20"><circle cx="10" cy="10" r="10" fill="#3d3e40"/><path d="M10 4.5a3.6 3.6 0 0 0-3.6 3.6c0 2.6 3.6 7 3.6 7s3.6-4.4 3.6-7A3.6 3.6 0 0 0 10 4.5z" fill="#7dc242"/><circle cx="10" cy="8.1" r="1.3" fill="#3d3e40"/></svg>
        <span>20917 - 87 Ave. Edmonton, AB, Canada.<br>T6K 2R8</span>
      </p>
      <p class="contact contact--email">
        <svg viewBox="0 0 20 20"><circle cx="10" cy="10" r="10" fill="#3d3e40"/><circle cx="10" cy="10" r="5.5" fill="none" stroke="#7dc242" stroke-width="1.2"/><ellipse cx="10" cy="10" rx="2.3" ry="5.5" fill="none" stroke="#7dc242" stroke-width="1.1"/><path d="M4.5 10h11" stroke="#7dc242" stroke-width="1.1"/></svg>
        <span>helen.dovbush@mailvane.example</span>
      </p>
      <p class="contact contact--web">
        <svg viewBox="0 0 20 20"><circle cx="10" cy="10" r="10" fill="#3d3e40"/><rect x="5" y="6.5" width="10" height="7" rx="1" fill="#7dc242"/><path d="M5.3 7l4.7 3.6L14.7 7" fill="none" stroke="#3d3e40" stroke-width="1.1"/></svg>
        <span>www.qorvil.example</span>
      </p>
      <p class="contact contact--phone">
        <svg viewBox="0 0 20 20"><circle cx="10" cy="10" r="10" fill="#3d3e40"/><path d="M6.8 5.2l1.8-.4 1.1 2.7-1.2 1a7 7 0 0 0 3 3l1-1.2 2.7 1.1-.4 1.8c-.2.6-.8 1-1.5.9A9 9 0 0 1 5.9 6.7c-.1-.7.3-1.3.9-1.5z" fill="#7dc242"/></svg>
        <span>780.555.0187</span>
      </p>
      <p class="contact contact--mobile">
        <svg viewBox="0 0 20 20"><circle cx="10" cy="10" r="10" fill="#3d3e40"/><rect x="7" y="4.5" width="6" height="11" rx="1.2" fill="#7dc242"/><rect x="8" y="6" width="4" height="6.5" fill="#3d3e40"/><circle cx="10" cy="14" r=".7" fill="#3d3e40"/></svg>
        <span>780.555.0142</span>
      </p>
    </div>
  </section>

  <section class="card card--back" aria-label="Business card back">
    <div class="brand">
      <div class="brand__row">
        <div class="brand__dot"></div>
        <div class="brand__name">qorvil</div>
      </div>
      <div class="brand__tagline">Electrical Wholesalers</div>
    </div>
    <p class="back__web">WWW.QORVIL.EXAMPLE</p>
  </section>

</main>
</body>
</html>
```